PSD Website Design

I am looking to have a custom website designed. I would like a PSD made of the design I came up with. Once I get the design I will slice the PSD and create a wordpress template from it.

See attachment for basic layout of the graphic. The image labeled Player page is the basic page I will need for the website. I also need a home page with an image slider on it and thumbnails of recent, state video uploads.

A textured background is ok.

Looking for a quick turnaround.

Text at top of page is a menu that is needed. Open to seeing the menu as a navigational bar or/and with different font types.

No preference on page background color or font colors. I welcome creativity.

```html
<!DOCTYPE html>
<html lang="en">
<head>
<meta charset="utf-8">
<title>Summit Recruiting – Player Profile</title>
<link href="https://fonts.googleapis.com/css2?family=Oswald:wght@400;500;600&family=Open+Sans:wght@400;600;700&display=swap" rel="stylesheet">
<style>
:root{
  --orange:#e8760f;
  --red:#d6322c;
  --red-dark:#9e1f1b;
  --ink:#222;
  --link-blue:#2a63b8;
  --page-bg:#dcdde0;
  --panel:#fff;
  --footer:#3a3a3a;
  --footer-bottom:#1f1f1f;
  --sky:#6cc6ec;
  --olive:#6b8a1f;
}
*{box-sizing:border-box;margin:0;padding:0}
html,body{width:843px;height:1200px;overflow:hidden}
body{position:relative;background:var(--page-bg);font-family:"Open Sans",sans-serif;color:var(--ink)}
.abs{position:absolute}
.header{left:0;top:0;width:843px;height:64px;background:#fff}
.header-rule{left:0;top:64px;width:843px;height:6px;background:var(--orange)}
.brand{left:80px;top:22px;display:flex;align-items:center;gap:7px}
.brand-mark{width:16px;height:16px;background:var(--orange)}
.brand-name{font-family:"Oswald",sans-serif;font-weight:600;font-size:18px;line-height:22px;color:var(--ink);letter-spacing:.5px}
.nav a{position:absolute;top:29px;font-size:14px;color:#666;text-decoration:none}
.nav a.active{color:var(--orange)}
.nav-caret{left:543px;top:58px;width:0;height:0;border-left:6px solid transparent;border-right:6px solid transparent;border-bottom:6px solid var(--orange)}
.search{left:654px;top:28px;width:100px;height:21px;border:1px solid #bbb;background:#eee;border-radius:2px}
.search span{position:absolute;left:8px;top:3px;font-size:10px;font-style:italic;color:#999}
.search i{position:absolute;right:0;top:0;width:23px;height:19px;background:#d5d5d5;border-left:1px solid #bbb}
.panel{left:74px;top:78px;width:686px;height:912px;background:var(--panel)}
.photo-frame{left:86px;top:100px;width:178px;height:218px;background:#fff;box-shadow:0 2px 6px rgba(0,0,0,.35);transform:rotate(-2deg);padding:8px}
.photo{width:100%;height:100%;background:linear-gradient(160deg,#d9ebb0,#c7de8a 60%,#b9cf7e)}
.player-name{left:278px;top:98px;font-size:19px;font-weight:600}
.player-pos{left:278px;top:124px;font-size:10px;font-weight:600;color:var(--link-blue)}
.stats{left:278px;top:140px;font-size:9px;line-height:14.5px;color:#333}
.class-of{left:275px;top:282px;font-family:"Oswald",sans-serif;font-size:11px;color:var(--olive);letter-spacing:.5px}
.ribbon-line{height:3px;background:#555}
.ribbon{height:54px}
.ribbon span{position:absolute;left:0;width:100%;top:14px;text-align:center;font-family:"Oswald",sans-serif;font-size:16px;line-height:20px;color:#fff;letter-spacing:-.2px}
.thumb{width:93px;height:52px}
.thumb-time{position:absolute;right:2px;bottom:2px;background:rgba(0,0,0,.8);color:#fff;font-size:6px;padding:0 2px}
.vt{width:93px;font-size:6.5px;line-height:8.5px;color:var(--link-blue)}
.vm{display:block;color:#888;font-size:5.5px;line-height:7px;margin-top:2px}
.channel{left:460px;top:257px;font-size:8px;font-weight:600;display:flex;align-items:center;gap:4px}
.channel small{font-weight:400;color:#999;font-size:6px}
.channel i{width:9px;height:9px;border-radius:50%;background:#222;display:inline-block}
.section-title{font-family:"Oswald",sans-serif;font-size:16px;line-height:22px;color:var(--orange);background:#fff;padding:0 5px}
.orange-line{height:2px;background:linear-gradient(90deg,var(--orange),var(--orange) 80%,rgba(232,118,15,0))}
.video{left:87px;top:405px;width:383px;height:235px;box-shadow:0 5px 8px rgba(0,0,0,.25)}
.video-frame{position:absolute;left:0;top:0;width:383px;height:215px;background:linear-gradient(180deg,#e9eaec 0%,#cfd1d2 30%,#6a2a30 60%,#2a1d22 100%)}
.controls{position:absolute;left:0;bottom:0;width:100%;height:20px;background:linear-gradient(#2c2c2c,#111);color:#bbb;font-size:6px;display:flex;align-items:center;padding-left:60px}
.controls::before{content:"";position:absolute;left:0;top:0;width:100%;height:2px;background:#555}
.ad{left:535px;top:405px;width:211px;height:211px;background:#c6c6c6;display:flex;align-items:center;justify-content:center;font-family:"Oswald",sans-serif;font-size:19px;color:#fff}
.event-box{left:94px;top:724px;width:248px;height:236px;background:#262626;border-radius:2px}
.event-tab{left:108px;top:740px;width:82px;height:22px;background:#fff;font-family:"Oswald",sans-serif;font-size:15px;line-height:22px;padding-left:2px;color:#111}
.event-body{left:106px;top:760px;width:223px;height:72px;background:#fff;border-radius:2px;font-size:10.5px;line-height:15px;padding:6px 0 0 6px}
.connect{left:79px;top:846px;width:251px;height:28px;background:var(--sky);font-family:"Oswald",sans-serif;font-size:15px;line-height:24px;color:#fff;padding-left:30px}
.connect-fold{left:79px;top:874px;width:0;height:0;border-top:12px solid #3a86a6;border-left:14px solid transparent}
.social{top:890px;width:45px;height:45px;border-radius:5px;background:linear-gradient(#f4f4f4,#cfcfcf);border-bottom:3px solid var(--sky)}
.recruit-video{left:361px;top:724px;width:388px;height:236px;background:#000}
.spinner{left:547px;top:827px;width:16px;height:16px;border-radius:50%;border:3px dotted #bbb}
.footer{left:0;top:990px;width:843px;height:182px;background:var(--footer);border-top:4px solid var(--orange)}
.footer-bottom{left:0;top:1172px;width:843px;height:28px;background:var(--footer-bottom);color:#ddd;font-size:11px;padding:7px 0 0 82px}
.f-title{font-family:"Oswald",sans-serif;font-size:17px;color:var(--orange)}
.f-rule{height:1px;background:linear-gradient(90deg,#555,#555 70%,rgba(85,85,85,0))}
.f-links a{display:block;color:#eee;font-size:12px;text-decoration:none;line-height:21.7px}
.contact-row{color:#eee;font-size:12px;display:flex;gap:10px;align-items:flex-start;line-height:15px}
.field{background:#7a7a7a;border:1px solid #999;color:#eee;font-size:11px;font-style:italic;padding:3px 7px}
.send{left:690px;top:1135px;width:60px;height:21px;background:var(--orange);color:#fff;font-size:12px;text-align:center;line-height:21px}
</style>
</head>
<body>
<header class="abs header"></header>
<div class="abs header-rule"></div>
<div class="abs brand"><span class="brand-mark"></span><span class="brand-name">SUMMIT RECRUITING</span></div>
<nav class="nav">
  <a style="left:319px">Home</a><a style="left:387px">About us</a><a style="left:469px">State</a><a class="active" style="left:524px">Position</a><a style="left:601px">Join</a>
</nav>
<div class="abs nav-caret"></div>
<div class="abs search"><span>search here...</span><i></i></div>

<main class="abs panel"></main>

<div class="abs photo-frame"><div class="photo" role="img" aria-label="Player portrait photo"></div></div>
<div class="abs player-name">Marcus Delaney</div>
<div class="abs player-pos">Wide Receiver</div>
<div class="abs stats">Miami, FL (Bayview High)<br>Ht: 6-1.5 &nbsp;|&nbsp; Wt: 197<br>40 Time: 4.45<br>Bench: 22 Reps<br>Vertical: 36<br>5-10-5 Shuttle: 4.42</div>
<div class="abs class-of">CLASS OF 2015</div>

<div class="abs ribbon-line" style="left:457px;top:109px;width:291px"></div>
<div class="abs ribbon" style="left:512px;top:88px;width:176px">
  <svg width="176" height="54" viewBox="0 0 176 54"><path d="M0 22 L24 2 L30 22Z" fill="var(--red-dark)"/><path d="M176 22 L152 2 L146 22Z" fill="var(--red-dark)"/><path d="M22 2 H154 L142 40 Q138 50 126 50 H50 Q38 50 34 40Z" fill="var(--red)" stroke="#fff" stroke-width="2"/></svg>
  <span>GAME FILM</span>
</div>

<div class="abs thumb" style="left:460px;top:150px;background:linear-gradient(#7aa05a,#4d6a3a)" role="img" aria-label="Video thumbnail: model railway"><span class="thumb-time">9:56</span></div>
<div class="abs thumb" style="left:558px;top:150px;background:linear-gradient(#8a9a6a,#5b5f4a)" role="img" aria-label="Video thumbnail: garden railway"><span class="thumb-time">7:54</span></div>
<div class="abs thumb" style="left:656px;top:150px;background:linear-gradient(#9aa7a2,#4f5a45)" role="img" aria-label="Video thumbnail: steam train"><span class="thumb-time">6:23</span></div>
<div class="abs vt" style="left:460px;top:207px">Rail Parade and Other Vintage Engines<span class="vm">by railfan · 10,820 views<br>3 years ago</span></div>
<div class="abs vt" style="left:558px;top:207px">Coupling Test Run<span class="vm">by yardmaster · 10,358 views<br>3 years ago</span></div>
<div class="abs vt" style="left:656px;top:207px">Steam Photo Train With Double Header<span class="vm">by lineside · 32,118 views<br>4 years ago</span></div>
<div class="abs" style="left:460px;top:249px;width:289px;height:1px;background:#e5e5e5"></div>
<div class="abs channel"><i></i>tracksidetv <small>Popular channel - you might like it</small></div>
<div class="abs thumb" style="left:460px;top:274px;background:linear-gradient(#3aa0e0,#c2332b)" role="img" aria-label="Video thumbnail: toy trains"><span class="thumb-time">23:45</span></div>
<div class="abs thumb" style="left:558px;top:274px;background:linear-gradient(#d9c8b0,#8e6f55)" role="img" aria-label="Video thumbnail: toy vacuum"><span class="thumb-time">4:47</span></div>
<div class="abs thumb" style="left:656px;top:274px;background:linear-gradient(#5aa8e8,#3b8a3a)" role="img" aria-label="Video thumbnail: toy train set"><span class="thumb-time">13:33</span></div>
<div class="abs vt" style="left:460px;top:330px">Little Engine Track Builder Ultimate R...<span class="vm">by tracksidetv · 17,498 views<br>1 year ago</span></div>
<div class="abs vt" style="left:558px;top:330px">Big Spider Meets Daddy Vacuum Shooter<span class="vm">by tracksidetv · 4,842 views<br>2 years ago</span></div>
<div class="abs vt" style="left:656px;top:330px">Toy Train Candy Mash Up &amp; Fun Play ...<span class="vm">by tracksidetv · 10,769 views<br>2 years ago</span></div>

<div class="abs orange-line" style="left:86px;top:381px;width:390px"></div>
<div class="abs section-title" style="left:105px;top:371px">HIGHLIGHTS</div>
<div class="abs video">
  <div class="video-frame" role="img" aria-label="Highlight video: team gathered on indoor field"></div>
  <div class="controls">0:12 / 7:50</div>
</div>
<div class="abs ad">ADVERTISEMENT SPOT</div>

<div class="abs orange-line" style="left:86px;top:691px;width:266px"></div>
<div class="abs section-title" style="left:103px;top:681px">TAKE IT VIRAL</div>
<div class="abs ribbon-line" style="left:361px;top:689px;width:386px"></div>
<div class="abs ribbon" style="left:456px;top:666px;width:200px">
  <svg width="200" height="54" viewBox="0 0 200 54"><path d="M0 22 L24 2 L30 22Z" fill="var(--red-dark)"/><path d="M200 22 L176 2 L170 22Z" fill="var(--red-dark)"/><path d="M22 2 H178 L166 40 Q162 50 150 50 H50 Q38 50 34 40Z" fill="var(--red)" stroke="#fff" stroke-width="2"/></svg>
  <span>RECENT RECRUITS</span>
</div>

<div class="abs event-box"></div>
<div class="abs event-body">Lorem ipsum dolor sit amet,consectetuer adipiscing elit, sed diam nonummy nibh euismod tincidunt ut laoreet dolore magna aliquam erat volutpat.</div>
<div class="abs event-tab">NEXT EVENT</div>
<div class="abs connect">CONNECT WITH HUDDLE</div>
<div class="abs connect-fold"></div>
<div class="abs social" style="left:108px" role="img" aria-label="Social link"></div>
<div class="abs social" style="left:166px" role="img" aria-label="Social link"></div>
<div class="abs social" style="left:225px" role="img" aria-label="Social link"></div>
<div class="abs social" style="left:282px" role="img" aria-label="Social link"></div>

<div class="abs recruit-video">
  <div class="controls" style="padding-left:56px">0:00 / 1:36</div>
</div>
<div class="abs spinner"></div>

<footer class="abs footer"></footer>
<div class="abs f-title" style="left:100px;top:1010px">QUICK LINKS</div>
<div class="abs f-rule" style="left:80px;top:1039px;width:140px"></div>
<div class="abs f-links" style="left:98px;top:1043px"><a>About us</a><a>Position</a><a>State</a><a>Join</a></div>
<div class="abs f-title" style="left:290px;top:1010px">CONTACT US</div>
<div class="abs f-rule" style="left:272px;top:1039px;width:170px"></div>
<div class="abs contact-row" style="left:274px;top:1046px"><svg width="12" height="14" viewBox="0 0 12 14"><path d="M6 0a5 5 0 0 0-5 5c0 4 5 9 5 9s5-5 5-9a5 5 0 0 0-5-5z" fill="#999"/><circle cx="6" cy="5" r="2" fill="#3a3a3a"/></svg><span>Address: 88 Field Lane,<br>Oakridge, ST 40210</span></div>
<div class="abs contact-row" style="left:274px;top:1088px"><svg width="12" height="12" viewBox="0 0 12 12"><path d="M2 0l2 3-1 1.5c1 2 2.5 3.5 4.5 4.5L9 8l3 2-1 2C5 12 0 7 0 1z" fill="#999"/></svg><span>555-0142-7789</span></div>
<div class="abs contact-row" style="left:274px;top:1115px"><svg width="13" height="10" viewBox="0 0 13 10"><rect x=".5" y=".5" width="12" height="9" fill="none" stroke="#999"/><path d="M.5.5 6.5 6 12.5.5" fill="none" stroke="#999"/></svg><span>hello@summitrecruit.example</span></div>
<div class="abs f-title" style="left:538px;top:1010px">GET IN TOUCH</div>
<div class="abs field" style="left:539px;top:1044px;width:91px;height:20px">Name</div>
<div class="abs field" style="left:644px;top:1044px;width:106px;height:20px">Email</div>
<div class="abs field" style="left:539px;top:1072px;width:211px;height:56px;padding-top:6px">Your Message...</div>
<div class="abs send">Send</div>
<div class="abs footer-bottom">© 2014 Summit Recruiting, All Rights Reserved</div>
</body>
</html>
```